Web design for our new company

We need a web design for our product and for our company.
And the main is our Product tool called "velmora".
----------------------------------------------------------
[Our company's Goal]
Make organization’s communication smooth and healthy with transparency and efficiency for works and tasks in all levels with our workflow tool.

[Our Mission]
Our mission is to achieve business goals with customers.
We work together to identify the goals for your company, guides your strategy and bring the technology answers which best fit to achieve the goals.

[What we do]
We have a workflow tool "velmora"
- Very simple end-user configurable workflow for any company processes
(Targeting small-med size company)
- Graphical & fun features for startup users
- Simple and easy task control with quillbox e-mail look & feel
- Non charged skill up guidance
- Additional features with;
Multiple delegation
Clear status for each owner
Task owner management console with due date reminders&reporting

Others
1. System Development & Implementation Service
Our client list includes a wide variety of small to medium to major sized enterprises.
We can offer from full-scratch based development to packaged system implementation.

2. Project Management(PM) Service
We will provide end-to-end PM service with experienced PM.
Our service is not only “managing” but “leading” to bring success to achieve the goal.

3.Consultation Service

Consulting services to a wide range of fields such as creating business strategy, business process Kaizen, IT system consultation and change management.

Target Market(s)

Business to Business
Mainly to medium size - startup company

Industry/Entity Type

It Company

Coding

Coded - Design and coding required

Number of Pages Required

5+ page

Colors
0255a3
33a6d7
86cfc6
33b8a4
add136
cadf82
fbf289
fee18a
faa54b

Requirements
Must have
• We need Pages for
• Company mission
• Service Overview
• Contact
• Privacy Policy
• Terms and Conditions
• =========================
• As there were some questions, I add followings.---------
• 1. File Format
• We are going to use Brixel cloud services to upload finished web files.
• The finished files should be ready to use by simply replacing images and text.
• Please provide me "easy to handle" template with "sophisticated design".
• Thanks!
• 2. Multiple Languages
• We need buttons for changing language.
• We will have this translated to German, English and Japanese.
• Thank you so much!!
Nice to have
• These are current Logos and will be a next project to revise them...
• Attached Company Profile and Logo design
• 1. Company Profile
• 2. Our Company Logo
• 3. Our Product Logo -> This is most close to our image of design base.
• 4. Product Logo for PPT Header
• All just for your reference.
• ---------
• As there were some request, I added attachment as for contents for Our mission page.
Should not have
• I hope to see some unique designs.
• (Sorry please ignore my last update as I checked with our CEO.
• Bootstrap is absolutely good template.)

```html
<!DOCTYPE html>
<html lang="en">
<head>
<meta charset="utf-8">
<title>TAVRIO – Workflow Tools &amp; Services</title>
<link href="https://fonts.googleapis.com/css2?family=Lato:ital,wght@0,400;0,700;0,900;1,400&display=swap" rel="stylesheet">
<style>
:root{
  --navy:#0255a3;
  --sky:#33a6d7;
  --teal:#33b8a4;
  --lime:#add136;
  --orange:#faa54b;
  --orange-strong:#f79433;
  --ink:#333;
  --muted:#555;
  --white:#fff;
}
*{margin:0;padding:0;box-sizing:border-box}
html,body{width:678px;height:1200px;overflow:hidden;background:#fff}
body{font-family:'Lato',sans-serif;color:var(--ink);position:relative}
.site-header{height:82px;position:relative}
.brand{position:absolute;left:42px;top:22px;display:flex;align-items:center;gap:6px;font-weight:900;font-size:15px;color:var(--lime)}
.brand-dot{width:12px;height:12px;border-radius:50%;background:var(--lime)}
.social{position:absolute;left:334px;top:22px;display:flex;gap:9px}
.social span{width:12px;height:12px;border-radius:50%;background:var(--navy);display:block}
.search{position:absolute;left:464px;top:19px;width:121px;height:19px;border:1px solid #bbb;font-size:8px;color:#666;padding:4px 6px}
.search svg{position:absolute;right:5px;top:4px}
.lang{position:absolute;left:598px;top:23px;font-size:7px;display:flex;align-items:center;gap:5px;color:#333}
.flag{width:13px;height:9px;background:var(--navy);position:relative;overflow:hidden}
.flag::before{content:"";position:absolute;left:0;top:3px;width:13px;height:3px;background:#d22}
.flag::after{content:"";position:absolute;left:5px;top:0;width:3px;height:9px;background:#d22}
.main-nav{position:absolute;left:260px;top:50px;display:flex;font-size:7.5px;font-weight:700;text-transform:uppercase}
.main-nav a{color:#222;text-decoration:none;padding:6px 10px;margin-right:5px}
.main-nav a.active{background:var(--orange-strong);color:#fff}
.hero{position:absolute;top:82px;left:0;width:678px;height:298px;background:linear-gradient(110deg,#b9bfc6 0%,#8e969e 45%,#d9dde2 70%,#a9b2ba 100%);text-align:center;color:#fff}
.hero h1{font-size:33px;font-weight:900;margin-top:72px;text-shadow:0 1px 3px rgba(0,0,0,.3)}
.hero p{font-size:13.5px;font-weight:700;width:420px;margin:6px auto 0;line-height:17px;text-shadow:0 1px 3px rgba(0,0,0,.4)}
.btn{display:inline-block;margin-top:15px;background:var(--orange-strong);color:#fff;font-size:9.5px;font-weight:700;padding:7px 20px;text-transform:uppercase}
.dots{position:absolute;left:318px;top:270px;display:flex;gap:6px}
.dots span{width:6px;height:6px;border-radius:50%;background:#fff}
.dots span:first-child{background:var(--teal)}
.mission{position:absolute;top:380px;width:678px;height:146px;text-align:center}
.section-title{font-size:19px;font-weight:400;color:var(--navy)}
.mission .section-title{margin-top:34px}
.mission p{font-size:9px;line-height:16px;margin-top:12px;color:#333}
.services{position:absolute;top:526px;width:678px;height:256px;background:linear-gradient(90deg,var(--teal),#2b8fd0);color:#fff;text-align:center}
.services .section-title{color:#fff;margin-top:28px}
.service-list{display:flex;justify-content:space-between;padding:0 40px;margin-top:24px}
.service{width:188px}
.service svg{height:38px}
.service h3{font-size:12px;font-weight:400;line-height:16px;margin-top:10px}
.service p{font-size:7.5px;line-height:13px;margin-top:7px}
.products{position:absolute;top:782px;width:678px;height:254px}
.products .section-title{position:absolute;left:42px;top:32px}
.products h4{position:absolute;left:42px;top:67px;font-size:12px;color:var(--orange-strong);font-weight:400}
.products h4 b{color:var(--navy);font-weight:900}
.features{position:absolute;left:42px;top:86px;list-style:none;font-size:7.5px;color:#333}
.features li{position:relative;padding-left:19px;margin-bottom:6.5px;line-height:11px}
.features li::before{content:"";position:absolute;left:0;top:2px;width:8px;height:8px;border-radius:50%;background:var(--navy)}
.features li::after{content:"";position:absolute;left:2.3px;top:3.6px;width:2.5px;height:4px;border:solid #fff;border-width:0 1.2px 1.2px 0;transform:rotate(45deg)}
.features li.accent{color:var(--navy);font-weight:700}
.features em{display:block}
.product-photo{position:absolute;left:350px;top:0;width:325px;height:254px;background:linear-gradient(180deg,#3a3d42,#1d1f23)}
.tablet{position:absolute;left:418px;top:870px;width:180px;height:128px;background:#222;border-radius:6px}
.tablet-screen{position:absolute;left:15px;top:13px;width:150px;height:112px;background:#fff;display:flex;align-items:center;justify-content:center;gap:5px;font-size:17px;font-weight:900;color:var(--navy)}
.tablet-screen i{width:12px;height:12px;background:var(--navy);display:block}
.site-footer{position:absolute;top:1036px;width:678px;height:164px;background:linear-gradient(90deg,#0a4b9a 0%,#2a7a7c 50%,var(--lime) 100%);color:#fff}
.footer-brand{position:absolute;left:42px;top:42px;display:flex;align-items:center;gap:6px;font-weight:900;font-size:15px}
.footer-brand i{width:12px;height:12px;border-radius:50%;background:#fff;display:block}
.copyright{position:absolute;left:42px;top:114px;font-size:7.5px;line-height:11.5px}
.footer-col{position:absolute;top:30px;font-size:7.5px}
.footer-col h5{font-size:8px;font-weight:900;margin-bottom:9px;text-transform:uppercase}
.footer-col a{display:block;color:#fff;text-decoration:none;margin-bottom:8px}
.sitemap-grid{display:grid;grid-template-columns:56px 70px}
.contact p{margin-bottom:5px;line-height:11.5px;display:flex;align-items:flex-start;gap:5px}
.contact strong{font-weight:900}
.corner{position:absolute;right:8px;bottom:14px;font-size:7px}
</style>
</head>
<body>
<header class="site-header">
  <div class="brand"><span class="brand-dot"></span>TAVRIO</div>
  <div class="social" aria-label="Social links"><span></span><span></span><span></span><span></span><span></span><span></span></div>
  <div class="search">Search
    <svg width="8" height="8" viewBox="0 0 10 10"><circle cx="4" cy="4" r="3" fill="none" stroke="#8aa83a" stroke-width="1.4"/><line x1="6.2" y1="6.2" x2="9" y2="9" stroke="#8aa83a" stroke-width="1.4"/></svg>
  </div>
  <div class="lang"><span class="flag"></span>EN <span>&#8964;</span></div>
  <nav class="main-nav">
    <a class="active" href="#">Home</a><a href="#">Mission</a><a href="#">Services</a><a href="#">Contact</a><a href="#">Privacy</a><a href="#">Terms &amp; Conditions</a>
  </nav>
</header>

<section class="hero" role="img" aria-label="Person at a desk reviewing a project timeline chart on a monitor">
  <h1>TAVRIO</h1>
  <p>Make organization’s communication smooth and healthy with transparency and efficiency for works and tasks in all levels with our workflow tool.</p>
  <span class="btn">Read More</span>
  <div class="dots"><span></span><span></span><span></span><span></span></div>
</section>

<section class="mission">
  <h2 class="section-title">Our Mission</h2>
  <p>Our mission is to achieve business goals with customers.<br>We work together to identify the goals for your company, guides your strategy and bring the<br>technology answers which best fit to achieve the goals.</p>
</section>

<section class="services">
  <h2 class="section-title">What We Do</h2>
  <div class="service-list">
    <div class="service">
      <svg viewBox="0 0 50 38" width="50"><rect x="7" y="3" width="36" height="24" rx="2" fill="none" stroke="#fff" stroke-width="3"/><rect x="1" y="30" width="48" height="4" rx="2" fill="#fff"/></svg>
      <h3>Project Management(PM)<br>Service</h3>
      <p>We will provide end-to-end PM service with experienced PM. Our service is not only “managing” but “leading” to bring success to achieve the goal.</p>
    </div>
    <div class="service">
      <svg viewBox="0 0 44 40" width="44"><circle cx="15" cy="22" r="9" fill="none" stroke="#fff" stroke-width="6" stroke-dasharray="4 3"/><circle cx="15" cy="22" r="4" fill="#fff"/><circle cx="33" cy="10" r="6" fill="none" stroke="#fff" stroke-width="4" stroke-dasharray="3 2"/><circle cx="33" cy="31" r="6" fill="none" stroke="#fff" stroke-width="4" stroke-dasharray="3 2"/></svg>
      <h3>System Development<br>&amp; Implementation Service</h3>
      <p>Our client list includes a wide variety of small to medium to major sized enterprises. We can offer from full-scratch based development to packaged system implementation.</p>
    </div>
    <div class="service">
      <svg viewBox="0 0 44 34" width="42"><ellipse cx="17" cy="13" rx="16" ry="11" fill="#fff"/><path d="M6 21 L3 29 L13 23Z" fill="#fff"/><ellipse cx="30" cy="20" rx="13" ry="9" fill="#fff" stroke="#2ca0c4" stroke-width="2"/><path d="M37 27 L41 33 L32 28Z" fill="#fff"/></svg>
      <h3>Consultation<br>Service</h3>
      <p>Consulting services to a wide range of fields such as creating business strategy, business process Kaizen, IT system consultation and change management.</p>
    </div>
  </div>
</section>

<section class="products">
  <h2 class="section-title">Our Products</h2>
  <h4>We have a workflow tool <b>"velmora"</b></h4>
  <ul class="features">
    <li>Very simple end-user configurable workflow for any company processes<em>(Targeting small-med size company)</em></li>
    <li>Graphical &amp; fun features for startup users</li>
    <li>Simple and easy task control with quillbox e-mail look &amp; feel</li>
    <li>Non charged skill up guidance</li>
    <li class="accent">Additional features with;</li>
    <li>Multiple delegation</li>
    <li>Clear status for each owner</li>
    <li>Task owner management console with due date reminders &amp; reporting</li>
  </ul>
  <div class="product-photo" role="img" aria-label="Businessman in a dark suit holding a tablet"></div>
</section>
<div class="tablet"><div class="tablet-screen">velmora<i></i></div></div>

<footer class="site-footer">
  <div class="footer-brand"><i></i>TAVRIO</div>
  <p class="copyright">Copyright © 2018. Company Name<br>All Right Reserved</p>
  <div class="footer-col" style="left:206px">
    <h5>Site Map</h5>
    <div class="sitemap-grid"><a href="#">Home</a><a href="#">Contact</a><a href="#">Mission</a><a href="#">Privacy</a><a href="#">Services</a><a href="#">Terms &amp; Conditions</a></div>
  </div>
  <div class="footer-col" style="left:379px">
    <h5>Services</h5>
    <a href="#">Pellentesque</a><a href="#">Purus in porta</a><a href="#">Malesuada</a><a href="#">Nisl tristique nisl</a><a href="#">Tturpis</a>
  </div>
  <div class="footer-col contact" style="left:500px">
    <h5>Contact Locations</h5>
    <p><strong>TAVRIO</strong></p>
    <p>412 Fenwick Lane,<br>Carrowby, K17 3PL</p>
    <p><svg width="7" height="7" viewBox="0 0 10 10"><path d="M2 1h2l1 2.5-1.3 1a6 6 0 0 0 2.8 2.8l1-1.3L10 7v2a1 1 0 0 1-1 1A9 9 0 0 1 0 2a1 1 0 0 1 1-1z" fill="#fff"/></svg>1-800-555-0142</p>
    <p><svg width="8" height="7" viewBox="0 0 10 8"><rect width="10" height="8" fill="#fff"/><path d="M0 0l5 4 5-4" fill="none" stroke="#3b8a6e" stroke-width="1"/></svg>hello@tavrio.example</p>
    <p><svg width="6" height="8" viewBox="0 0 8 11"><path d="M4 0a4 4 0 0 1 4 4c0 3-4 7-4 7S0 7 0 4a4 4 0 0 1 4-4z" fill="#fff"/><circle cx="4" cy="4" r="1.4" fill="#3b8a6e"/></svg>&nbsp;Map Direction</p>
  </div>
  <span class="corner">X10</span>
</footer>
</body>
</html>
```